New Word Template Design Project

I need this document for death certificate ordering to look like our branding. I will attach the pdf with the information and a sample pdf of our style. I also think that check boxes and x's would be better than yes and no.

2nd page in spanish.

Industry/Entity Type

Funeral

Requirements
Should not have
• Check boxes and red x's or yellow next to the yes, no , or sometimes

```html
<!DOCTYPE html>
<html lang="en">
<head>
<meta charset="utf-8">
<title>Death Certificate Ordering Guide – Alder Grove</title>
<link href="https://fonts.googleapis.com/css2?family=Jost:wght@400;500;600&display=swap" rel="stylesheet">
<style>
  :root{
    --bg:#eeeeee;
    --paper:#ffffff;
    --brand:#5585a5;
    --brand-deep:#2f4b6b;
    --accent-text:#3d6c94;
    --ink:#2a2a2a;
    --rule:#8a8a8a;
    --violet:#a08fb8;
    --gold:#d4a838;
  }
  *{box-sizing:border-box;margin:0;padding:0}
  html,body{width:1200px;height:1200px;overflow:hidden;background:var(--bg)}
  body{font-family:"Jost",sans-serif;color:var(--ink);position:relative}
  .sheet{position:absolute;left:150px;top:17px;width:900px;height:1165px;background:var(--paper);overflow:hidden}
  .brand{position:absolute;left:680px;top:70px;width:175px;text-align:center}
  .brand-name{display:flex;align-items:center;justify-content:center;gap:6px;font-size:25px;font-weight:500;color:var(--brand-deep);line-height:1}
  .brand-dot{width:9px;height:9px;border-radius:50%;background:var(--gold);flex:none}
  .brand-line{font-size:7px;letter-spacing:1.4px;color:var(--brand-deep);margin-top:8px;font-weight:500}
  .title{position:absolute;left:53px;top:94px;font-size:29px;font-weight:600;color:var(--brand)}
  .subtitle{position:absolute;left:53px;top:140px;font-size:22px;font-weight:600;color:var(--brand-deep)}
  .intro{position:absolute;left:53px;top:177px;width:793px;font-size:13.6px;line-height:21px}
  .uses{position:absolute;left:53px;top:263px;width:793px;border-collapse:collapse;font-size:13.6px}
  .uses th{background:var(--brand);color:#fff;font-weight:500;height:33px;text-align:center;font-size:14px;letter-spacing:.2px}
  .uses th:first-child{text-align:left;padding-left:8px}
  .uses th + th{border-left:1px solid #6f9ab7}
  .uses td{height:32.5px;border-bottom:1px solid var(--rule);text-align:center}
  .uses td:first-child{text-align:left;padding-left:8px}
  .uses tr td:first-child{border-left:1px solid var(--rule)}
  .uses tr td:last-child{border-right:1px solid var(--rule)}
  .col-use{width:284px}.col-orig{width:169px}.col-cause{width:142px}
  .box{display:inline-block;width:18px;height:18px;border:1.5px solid var(--brand);border-radius:3px;vertical-align:middle}
  .notes{position:absolute;top:775px;font-size:13.6px;line-height:21px}
  .notes.left{left:53px;width:370px;text-align:justify}
  .notes.right{left:476px;width:372px}
  .notes p{margin-bottom:8px}
  .hl{color:var(--accent-text)}
  .head{color:var(--brand-deep);font-weight:500}
  .list{list-style:none}
  .list li{position:relative;padding-left:14px}
  .list li::before{content:"";position:absolute;left:0;top:9px;width:4px;height:4px;border-radius:50%;background:var(--ink)}
  .choices li{line-height:24px}
  .choices li::before{top:10px}
  .contacts{display:grid;grid-template-columns:172px 1fr;padding-left:14px;position:relative}
  .contacts::before{content:"";position:absolute;left:0;top:9px;width:4px;height:4px;border-radius:50%;background:var(--ink)}
  .closing{position:absolute;left:0;right:0;top:1084px;text-align:center;font-size:17px;color:var(--accent-text)}
  .band{position:absolute;left:0;right:0;bottom:0;height:20px;background:linear-gradient(90deg,var(--brand),var(--violet),var(--gold))}
</style>
</head>
<body>
<main class="sheet">
  <div class="brand">
    <div class="brand-name"><span class="brand-dot"></span>Alder Grove</div>
    <div class="brand-line">FUNERAL &amp; CREMATION SERVICES</div>
  </div>

  <h1 class="title">Death Certificate Ordering Guide</h1>
  <h2 class="subtitle">Miami-Dade County</h2>

  <p class="intro">Certified death certificates are used to handle legal, financial, and personal matters after a loved one passes. While some institutions require an original, others may only need to view or copy it. In Florida, you can order death certificates with or without the cause of death. Cause of death is confidential and should only be included when necessary.</p>

  <table class="uses">
    <thead>
      <tr><th class="col-use">USE</th><th class="col-orig">ORIGINAL NEEDED?</th><th class="col-cause">WITH CAUSE?</th><th>SUGGESTED QUANTITY</th></tr>
    </thead>
    <tbody>
      <tr><td>Life Insurance Claims</td><td><span class="box"></span></td><td><span class="box"></span></td><td></td></tr>
      <tr><td>Pension or Retirement Benefits</td><td><span class="box"></span></td><td><span class="box"></span></td><td></td></tr>
      <tr><td>Investment / Brokerage Accounts</td><td><span class="box"></span></td><td><span class="box"></span></td><td></td></tr>
      <tr><td>Vehicle Title Transfer (DMV)</td><td><span class="box"></span></td><td><span class="box"></span></td><td></td></tr>
      <tr><td>Property / Real Estate Transfers</td><td><span class="box"></span></td><td><span class="box"></span></td><td></td></tr>
      <tr><td>Probate / Court Matters</td><td><span class="box"></span></td><td><span class="box"></span></td><td></td></tr>
      <tr><td>Social Security / Government Benefits</td><td><span class="box"></span></td><td><span class="box"></span></td><td></td></tr>
      <tr><td>Passport Cancellation / Consulates</td><td><span class="box"></span></td><td><span class="box"></span></td><td></td></tr>
      <tr><td>Domestic Travel with Cremated Remains</td><td><span class="box"></span></td><td><span class="box"></span></td><td></td></tr>
      <tr><td>International Travel with Cremated Remains</td><td><span class="box"></span></td><td><span class="box"></span></td><td></td></tr>
      <tr><td>Domestic Forwarding of Remains</td><td><span class="box"></span></td><td><span class="box"></span></td><td></td></tr>
      <tr><td>International Forwarding of Remains</td><td><span class="box"></span></td><td><span class="box"></span></td><td></td></tr>
      <tr><td>Credit Cards / Utility Companies</td><td><span class="box"></span></td><td><span class="box"></span></td><td></td></tr>
      <tr><td>Personal Copy / Peace of Mind</td><td><span class="box"></span></td><td><span class="box"></span></td><td></td></tr>
    </tbody>
  </table>

  <section class="notes left">
    <p><span class="head">Pricing (Miami-Dade County):</span><br>The first certified death certificate is <span class="hl">$20</span>, and each additional copy is <span class="hl">$16</span>.</p>
    <p>If you are <span class="hl">traveling domestically</span> or <span class="hl">internationally with cremated remains</span>, at least one certified copy is typically required. Some countries may require the certificate <span class="hl">with cause of death</span>. We will reach out to the consulate of the destination country to confirm the specific requirements for transporting cremated remains.</p>
    <p>Please note: <span class="hl">Other counties may have different pricing</span> for death certificates. We will inform you of the exact cost based on the location of death.</p>
  </section>

  <section class="notes right">
    <p><span class="hl">Most families order 4 to 8 certified copies.</span> A mix is common — for example, 2 with cause and 4 without cause. It simpler and more cost-effective to order them at the time of need. If you're unsure, we are here to guide you through the process.</p>
    <p class="head">How many certified copies would you like to order?</p>
    <ul class="list choices" style="margin-bottom:8px">
      <li>________ With Cause of Death</li>
      <li>________ Without Cause of Death</li>
    </ul>
    <p class="head" style="margin-bottom:0">Questions? We're Here for You</p>
    <ul class="list"><li>(305) 555-0142</li></ul>
    <div class="contacts">
      <span>westside@aldergrove.com</span><span>bayfront@aldergrove.com</span>
      <span>downtown@aldergrove.com</span><span>planahead@aldergrove.com</span>
    </div>
  </section>

  <p class="closing">Serving South Florida families with care, dignity, and support every day</p>
  <div class="band"></div>
</main>
</body>
</html>
```